Vero M.Q. - Diagnostic Ultrasound Flyer

About US
Vero M.Q. is a concierge ultrasound company that provides onsite or offsite diagnostic ultrasounds. We have over 14 years experience in sonography, business management, and customer service. We offer both the physician and patient flexibility, convenience, and access to timely services.

We provide ultrasounds for the following specialties:
Obstetrics/Gynecology
Abdominal
Small Parts
Vascular

Company Features:
1. Onsite or Offsite Scans
2. Images Available Immediately for Referring Physician and Patient
3. Flexible Options for Ultrasound Interpretation/Billing
4. Access to Interpreting Radiologist
5. Final Report Process - 1-2 Business Days/ 1 hour for STAT.
6. PACS Storage with Secure Access.

We need a place to add in our contact information (address, email, website, phone)

We already have a logo and would like to use it ( they are attached). We would the colors to match the logo colors....maybe lighter version of yellow and blue.

```html
<!DOCTYPE html>
<html lang="en">
<head>
<meta charset="utf-8">
<title>Vero M.Q. – Diagnostic Ultrasound Flyer</title>
<link href="https://fonts.googleapis.com/css2?family=Oswald:wght@300;400;500&family=Roboto+Condensed:wght@400;500&display=swap" rel="stylesheet">
<style>
  :root {
    --navy: #24337f;
    --gold: #f7bb33;
    --paper: #ffffff;
    --backdrop: #e2dfde;
    --photo-light: #d9d7d6;
    --photo-dark: #8f8c8b;
  }
  html, body {
    margin: 0;
    width: 1200px;
    height: 1200px;
    overflow: hidden;
    background: var(--backdrop);
  }
  .flyer {
    position: absolute;
    left: 211px;
    top: 50px;
    width: 451px;
    height: 638px;
    background: var(--paper);
    transform: scale(1.725);
    transform-origin: 0 0;
    overflow: hidden;
    font-family: "Roboto Condensed", sans-serif;
    color: var(--navy);
  }
  .flyer__shapes { position: absolute; inset: 0; }
  .brand {
    position: absolute;
    top: 27px;
    left: 0;
    width: 451px;
    display: flex;
    justify-content: center;
    align-items: center;
    gap: 6px;
  }
  .brand__dot {
    width: 9px; height: 9px; border-radius: 50%;
    background: var(--gold);
  }
  .brand__name {
    font-family: "Oswald", sans-serif;
    font-weight: 500;
    font-size: 24px;
    letter-spacing: 2px;
    color: var(--navy);
  }
  .heading {
    position: absolute;
    margin: 0;
    font-family: "Oswald", sans-serif;
    font-weight: 300;
    color: var(--navy);
    line-height: 1;
  }
  .about__title { left: 23px; top: 296px; font-size: 23px; }
  .about__text {
    position: absolute;
    left: 23px; top: 338px;
    margin: 0;
    font-size: 9.6px;
    line-height: 14.8px;
    white-space: nowrap;
  }
  .specialties__title { left: 23px; top: 416px; font-size: 22px; line-height: 29px; }
  .rule { position: absolute; left: 182px; width: 84px; height: 2px; background: var(--navy); }
  .rule--one { top: 428px; }
  .rule--two { top: 457px; }
  .specialties__list {
    position: absolute;
    left: 282px; top: 416px;
    margin: 0; padding: 0; list-style: none;
    font-size: 13.5px; line-height: 21.8px;
  }
  .specialties__list li { display: flex; align-items: center; gap: 6px; }
  .specialties__list li::before {
    content: ""; width: 4px; height: 9px;
    border-right: 1.5px solid var(--gold);
    border-radius: 0 6px 6px 0;
  }
  .features__band {
    position: absolute; left: 0; top: 506px;
    width: 208px; height: 32px; background: var(--gold);
  }
  .features__title { left: 23px; top: 509px; font-size: 22px; }
  .features__list {
    position: absolute; left: 23px; top: 543px;
    margin: 0; padding: 0; list-style: none;
    font-size: 7.4px; line-height: 14.5px;
    counter-reset: feature;
  }
  .features__list li { display: flex; align-items: center; gap: 4px; counter-increment: feature; }
  .features__list li::before {
    content: counter(feature);
    width: 8px; height: 8px; border-radius: 50%;
    background: var(--gold); color: var(--paper);
    font-size: 6px; line-height: 8px; text-align: center;
  }
  .contact {
    position: absolute; margin: 0; display: flex; align-items: center; gap: 8px;
    font-size: 8.2px; color: var(--navy);
  }
  .contact svg { width: 11px; height: 11px; fill: var(--navy); flex: none; }
  .contact--address { left: 332px; top: 560px; }
  .contact--email { left: 308px; top: 582px; }
  .contact--web { left: 286px; top: 599px; }
  .contact--phone { left: 268px; top: 615px; }
</style>
</head>
<body>
<main class="flyer">
  <svg class="flyer__shapes" viewBox="0 0 451 638" width="451" height="638">
    <defs>
      <linearGradient id="photoTone" x1="0" y1="0" x2="1" y2="1">
        <stop offset="0" stop-color="var(--photo-light)"/>
        <stop offset="0.6" stop-color="#bdb6b2"/>
        <stop offset="1" stop-color="var(--photo-dark)"/>
      </linearGradient>
    </defs>
    <polygon class="corner-stripe" points="0,0 14,0 240,100 225,100 0,8" fill="var(--gold)"/>
    <polygon class="corner-block" points="0,14 218,104 0,210" fill="var(--navy)"/>
    <polygon class="corner-sheen" points="240,100 451,8 451,100" fill="#ebeaea"/>
    <polygon class="hero-photo" role="img" aria-label="Photo of an expectant mother lying on an exam bed during an ultrasound scan"
             points="6,198 451,5 451,380" fill="url(#photoTone)"/>
    <polygon class="hero-band" points="0,198 451,386 451,400 0,210" fill="var(--navy)"/>
    <polygon class="about-block" points="0,214 285,330 0,330" fill="var(--gold)"/>
    <polygon class="footer-band" points="451,438 190,638 207,638 451,454" fill="var(--navy)"/>
    <polygon class="footer-block" points="451,462 216,638 451,638" fill="var(--gold)"/>
  </svg>

  <div class="brand"><span class="brand__dot"></span><span class="brand__name">VERO M.Q.</span></div>

  <h2 class="heading about__title">ABOUT US:</h2>
  <p class="about__text">Vero M.Q. is a concierge ultrasound company that provides<br>onsite or offsite diagnostic ultrasounds. We have over 14 years<br>experience in sonography, business management, and customer service. We<br>offer both the physician and patient flexibility, convenience, and access to timely<br>services.</p>

  <h2 class="heading specialties__title">WE PROVIDE<br>ULTRASOUNDS FOR<br>THE FOLLOWING SPECIALTIES:</h2>
  <span class="rule rule--one"></span>
  <span class="rule rule--two"></span>
  <ul class="specialties__list">
    <li>Obstetrics/Gynecology</li>
    <li>Abdominal</li>
    <li>Small Parts</li>
    <li>Vascular</li>
  </ul>

  <div class="features__band"></div>
  <h2 class="heading features__title">COMPANY FEATURES:</h2>
  <ol class="features__list">
    <li>Onsite or Offsite Scans</li>
    <li>Images Available Immediately for Referring Physician and Patient.</li>
    <li>Flexible Options for Ultrasound Interpretation/Billing</li>
    <li>Access to Interpreting Radiologist</li>
    <li>Final Report Process - 1-2 Business Days/ 1 hour for STAT.</li>
    <li>PACS Storage with Secure Access.</li>
  </ol>

  <p class="contact contact--address">
    <svg viewBox="0 0 24 24"><path d="M12 1a8 8 0 0 0-8 8c0 6 8 14 8 14s8-8 8-14a8 8 0 0 0-8-8zm0 11a3 3 0 1 1 0-6 3 3 0 0 1 0 6z"/></svg>
    Your Address.
  </p>
  <p class="contact contact--email">
    <svg viewBox="0 0 24 24"><path d="M2 5h20v14H2zm2 2v.5l8 5.5 8-5.5V7zm0 3v7h16v-7l-8 5.5z"/></svg>
    info@veromq.example
  </p>
  <p class="contact contact--web">
    <svg viewBox="0 0 24 24"><path d="M12 2a10 10 0 1 0 0 20 10 10 0 0 0 0-20zm0 2c1 1.2 1.9 3.3 2.2 7H9.8c.3-3.7 1.2-5.8 2.2-7zM4.1 11a8 8 0 0 1 3.7-5.9A16 16 0 0 0 7.8 11zm0 2h3.7a16 16 0 0 0 0 5.9A8 8 0 0 1 4.1 13zm5.7 0h4.4c-.3 3.7-1.2 5.8-2.2 7-1-1.2-1.9-3.3-2.2-7zm6.4 0h3.7a8 8 0 0 1-3.7 5.9 16 16 0 0 0 0-5.9zm0-2a16 16 0 0 0 0-5.9 8 8 0 0 1 3.7 5.9z"/></svg>
    www.veromq.example
  </p>
  <p class="contact contact--phone">
    <svg viewBox="0 0 24 24"><path d="M6.6 10.8a15 15 0 0 0 6.6 6.6l2.2-2.2a1 1 0 0 1 1-.25 11 11 0 0 0 3.6.6 1 1 0 0 1 1 1V20a1 1 0 0 1-1 1A17 17 0 0 1 3 4a1 1 0 0 1 1-1h3.5a1 1 0 0 1 1 1c0 1.25.2 2.45.6 3.6a1 1 0 0 1-.25 1z"/></svg>
    000 000 48213
  </p>
</main>
</body>
</html>
```